Town Planning business needs a design (template) for planning reports and letters

I'm looking to develop a report and a letter template. I prepare town planning reports in NSW, Australia. Fairly straight forward reports which would include figures and tables. I can provide examples of similar reports. I have a logo design which I can also provide ( I have attached one file).

Target Market(s)

Professionals, local and state governments

Industry/Entity Type

Property Development

Requirements
Must have
• Title page, contents, 3 - 4 levels of headings, tables and ability to inset figures/photos and Annexure pages at end of report
Nice to have
• Ability to include short details of project in header or footer

```html
<!DOCTYPE html>
<html lang="en">
<head>
<meta charset="utf-8">
<title>Urban Parcel – Report and Letter Templates</title>
<link href="https://fonts.googleapis.com/css2?family=Roboto:ital,wght@0,400;0,500;0,700;1,400&family=Montserrat:ital,wght@0,400;0,600;0,700;1,400&display=swap" rel="stylesheet">
<style>
:root{
  --blue:#0b6fc4;
  --blue-deep:#0a5ca6;
  --sky:#3aa8f2;
  --cyan:#13b4ee;
  --graphite:#5a5a5a;
  --mist:#c9c9c9;
  --ink:#1e2330;
  --sheet:#f0f6fc;
  --text:#6b6b6b;
  --canvas:#a3a3a3;
  --letter-dark:#3b3b3b;
  --navy:#1c2b4a;
  --row-alt:#e9eef3;
}
html,body{margin:0;width:1200px;height:1200px;overflow:hidden;background:var(--canvas)}
.stage{position:absolute;left:0;top:0;width:1932px;height:1932px;transform:scale(.62112);transform-origin:0 0;font-family:"Roboto",sans-serif}
.page{position:absolute;width:356px;height:510px;background:var(--sheet);overflow:hidden}
.page-title{position:absolute;left:11px;top:22px;margin:0;font:500 16px/20px "Roboto",sans-serif;color:var(--blue)}
.page-title::before{content:"";position:absolute;left:-11px;top:1px;width:4px;height:18px;background:var(--blue)}
.brand-tag{position:absolute;right:10px;top:10px;display:flex;align-items:center;gap:3px}
.brand-tag .mark{width:12px;height:12px;background:var(--blue)}
.brand-tag .name{font:700 5.5px/6px "Roboto",sans-serif;color:var(--blue);width:30px}
.copy{position:absolute;left:11px;right:18px;font-size:8.6px;line-height:13.5px;color:var(--text)}
.copy p{margin:0}
.sub-title{position:absolute;left:11px;margin:0;font:500 10px/12px "Roboto",sans-serif;color:var(--blue)}
.page-foot{position:absolute;left:0;right:0;bottom:0;height:25px;background:var(--ink);color:#fff;font-size:5px;line-height:7px;text-align:center;padding-top:5px;box-sizing:border-box}
.foot-tab{position:absolute;height:8px;width:70px;background:var(--blue)}

.cover-band{position:absolute;left:0;top:0;width:356px;height:382px;background:var(--blue)}
.rule{position:absolute;height:2px;background:#fff}
.cover-title{position:absolute;left:0;right:0;text-align:center;color:#fff}
.cover-title h1{margin:0;font:700 26px/30px "Roboto",sans-serif}
.cover-title .lede{font:400 16px/20px "Roboto",sans-serif}
.presenter{position:absolute;left:0;right:0;top:247px;text-align:center;color:#fff;font:400 11px/16px "Roboto",sans-serif}
.lockup{position:absolute;display:flex;align-items:center;gap:10px}
.lockup .mark{width:34px;height:34px}
.lockup .name{font:700 19px/22px "Montserrat",sans-serif;letter-spacing:.5px}

.bullets{position:absolute;left:11px;right:18px;top:288px;margin:0;padding:0;list-style:none;font-size:8.6px;line-height:13.5px;color:var(--text)}
.bullets li{position:relative;padding-left:16px;margin-bottom:4.5px}
.bullets li::before{content:"";position:absolute;left:2px;top:4px;width:5px;height:5px;background:var(--blue)}

.data-table{position:absolute;left:8px;top:150px;width:334px;border-collapse:separate;border-spacing:2px;font-size:4.6px;color:#333}
.data-table th{background:var(--blue);color:#fff;font-weight:500;height:14px;font-size:5px}
.data-table td{height:13px;text-align:center;background:#fff}
.data-table tr:nth-child(even) td{background:var(--row-alt)}
.data-table td:first-child{text-align:left;padding-left:10px;width:72px}
.dot{display:inline-block;width:4px;height:4px;border-radius:50%}
.d-b{background:var(--blue)}.d-g{background:#9a9a9a}.d-k{background:#555}

.photo{position:absolute}
.pair-title{margin:0;font:500 10px/12.5px "Roboto",sans-serif;color:var(--sky)}
.pair-copy{position:absolute;left:14px;width:166px;font-size:8.6px;line-height:13.5px;color:var(--text)}
.pair-copy p{margin:0}

.section-page{background:var(--blue-deep)}
.section-head{position:absolute;left:26px;color:#fff}
.section-head h2{margin:0;font:700 26px/30px "Roboto",sans-serif}
.section-head .lede{font:400 16px/20px "Roboto",sans-serif}

.legend{position:absolute;left:197px;font-size:5.4px;line-height:8px;color:#555;display:flex;gap:8px;width:140px}
.legend .swatch{flex:none;width:24px;height:22px}

.thanks{position:absolute;left:1511px;top:549px;width:354px;height:503px;background:var(--blue)}
.thanks .title{position:absolute;left:0;right:0;top:256px;text-align:center;color:#fff}
.thanks .title h2{margin:0;font:700 26px/30px "Roboto",sans-serif}
.thanks .title .lede{font:400 16px/20px "Roboto",sans-serif}
.thanks .address{position:absolute;left:0;right:0;top:334px;text-align:center;color:#fff;font:500 11px/16px "Roboto",sans-serif}
.thanks .fine{position:absolute;left:0;right:0;top:478px;text-align:center;color:#fff;font-size:5px;line-height:7px}

.letter{position:absolute;background:#fff;overflow:hidden;font-family:"Montserrat",sans-serif;color:var(--letter-dark)}
.recipient{position:absolute;font-size:6.4px;line-height:8.6px}
.recipient .to{font-style:italic;font-size:9px;line-height:11px;color:#444}
.recipient .who{font:700 11.5px/13px "Montserrat",sans-serif;color:var(--cyan)}
.recipient .role{font-style:italic;font-size:7px;line-height:10px;margin-bottom:4px}
.recipient .line{font-weight:600;color:var(--navy)}
.recipient .key{color:var(--cyan)}
.letter-date{position:absolute;font:italic 600 6.4px/8px "Montserrat",sans-serif;color:var(--navy)}
.letter-date .key{font-style:normal;color:var(--cyan);margin-right:4px}
.salutation{position:absolute;font:700 7.6px/10px "Montserrat",sans-serif;color:var(--navy)}
.letter-copy{position:absolute;font-size:8.2px;line-height:14px;text-align:justify;color:#4a4a4a}
.letter-copy p{margin:0 0 14px}
.sender{position:absolute}
.sender .from{font:italic 400 9px/11px "Montserrat",sans-serif}
.sender .who{font:700 11.5px/13px "Montserrat",sans-serif;color:var(--cyan)}
.sender .role{font:italic 400 7px/9px "Montserrat",sans-serif}
.signature{position:absolute;width:100px;height:22px;background:#eef3f7}
.sign-line{position:absolute;width:104px;height:1px;background:var(--letter-dark)}
.sign-label{position:absolute;font:400 7.6px/9px "Montserrat",sans-serif}
.letter-foot{position:absolute;left:0;right:0}
.contact{position:absolute;text-align:center;color:#fff;font-size:7.4px;line-height:11px}
.icon-ring{display:block;width:20px;height:20px;border-radius:50%;background:#fff;border:2px solid var(--cyan);box-sizing:border-box}
.icon-ring svg{display:block;width:12px;height:12px;margin:2px}
.contact-row{position:absolute;display:flex;align-items:center;gap:8px;color:#fff;font-size:7.4px;line-height:11px}
.contact-row .icon-ring{width:24px;height:24px;border-color:var(--navy)}
.contact-row .icon-ring svg{width:14px;height:14px;margin:3px}
</style>
</head>
<body>
<div class="stage">

  <section class="page" style="left:22px;top:23px;background:#fff">
    <div class="cover-band"></div>
    <div class="rule" style="left:60px;top:159px;width:236px"></div>
    <div class="cover-title" style="top:168px">
      <h1>Project Title here</h1>
      <div class="lede">Report sub details here</div>
    </div>
    <div class="rule" style="left:60px;top:231px;width:236px"></div>
    <div class="presenter">Persentator Name : ABC<br>Date: February 2023</div>
    <div class="lockup" style="left:106px;top:413px">
      <div class="mark" style="background:var(--blue)"></div>
      <div class="name" style="color:var(--navy)">URBAN<br>PARCEL</div>
    </div>
    <footer class="page-foot">Project summary: site address, lodgement reference and council area for this planning report.<br>Prepared for development assessment and review by local and state government authorities.</footer>
  </section>

  <section class="page" style="left:391px;top:23px">
    <h2 class="page-title">Main Heading Here</h2>
    <div class="brand-tag"><div class="mark"></div><div class="name">URBAN PARCEL</div></div>
    <div class="copy" style="top:50px"><p>Lorem Ipsum is simply dummy text of the printing and typesetting industry. Lorem Ipsum has been the industry's standard dummy text ever since the 1500s, when an unknown printer took a galley of type and scrambled it to make a type specimen book. It has survived not only five centuries, but also the leap into electronic typesetting, remaining essentially unchanged. It was popularised in the 1960s with the release of Presstype sheets containing Lorem Ipsum passages, and more recently with desktop publishing software like Folio LayoutPro including versions of Lorem Ipsum.</p></div>
    <h3 class="sub-title" style="top:155px">Subheading Text Title here</h3>
    <div class="copy" style="top:173px"><p>Lorem Ipsum is simply dummy text of the printing and typesetting industry. Lorem Ipsum has been the industry's standard dummy text ever since the 1500s, when an unknown printer took a galley of type and scrambled it to make a type specimen book. It has survived not only five centuries, but also the leap into electronic typesetting, remaining essentially unchanged. It was popularised in the 1960s with the release.</p></div>
    <h3 class="sub-title" style="top:267px">Bullet Points Text here</h3>
    <ul class="bullets">
      <li>Lorem Ipsum is simply dummy text of the printing and typesetting industry. Lorem Ipsum has been the industry's standard dummy</li>
      <li>Lorem Ipsum is simply dummy text of the printing and typesetting industry. Lorem Ipsum has been the industry's standard dummy</li>
      <li>Lorem Ipsum is simply dummy text of the printing and typesetting industry. Lorem Ipsum has been the industry's standard dummy</li>
      <li>Lorem Ipsum is simply dummy text of the printing and typesetting industry. Lorem Ipsum has been the industry's standard dummy</li>
      <li>Lorem Ipsum is simply dummy text of the printing and typesetting industry. Lorem Ipsum has been the industry's standard dummy</li>
    </ul>
    <footer class="page-foot">Project summary: site address, lodgement reference and council area for this planning report.<br>Prepared for development assessment and review by local and state government authorities.</footer>
  </section>

  <section class="page" style="left:765px;top:23px">
    <h2 class="page-title">Tabular Data</h2>
    <div class="brand-tag"><div class="mark"></div><div class="name">URBAN PARCEL</div></div>
    <div class="copy" style="top:54px"><p>Lorem Ipsum is simply dummy text of the printing and typesetting industry. Lorem Ipsum has been the industry's standard dummy text ever since the 1500s, when an unknown printer took a galley of type and scrambled it to Lorem Ipsum is simply dummy text of the printing and typesetting industry. Lorem Ipsum has been the industry's standard dummy text ever since the 1500s</p></div>
    <h3 class="sub-title" style="top:136px;font-size:8.6px">Table Data Title Here</h3>
    <table class="data-table">
      <tr><th>FEATURE DESCRIPTION</th><th>COLUMN TITLE</th><th>COLUMN TITLE</th><th>COLUMN TITLE</th><th>COLUMN TITLE</th></tr>
      <tr><td>First Row</td><td><span class="dot d-b"></span></td><td><span class="dot d-b"></span></td><td><span class="dot d-b"></span></td><td><span class="dot d-g"></span></td></tr>
      <tr><td>Second Row</td><td><span class="dot d-g"></span></td><td><span class="dot d-b"></span></td><td><span class="dot d-b"></span></td><td><span class="dot d-g"></span></td></tr>
      <tr><td>Third Row</td><td><span class="dot d-b"></span></td><td><span class="dot d-g"></span></td><td><span class="dot d-b"></span></td><td><span class="dot d-b"></span></td></tr>
      <tr><td>Rowmance</td><td><span class="dot d-b"></span></td><td><span class="dot d-g"></span></td><td><span class="dot d-b"></span></td><td><span class="dot d-b"></span></td></tr>
      <tr><td>Berow</td><td><span class="dot d-k"></span></td><td><span class="dot d-b"></span></td><td><span class="dot d-g"></span></td><td><span class="dot d-b"></span></td></tr>
      <tr><td>Rowanow</td><td><span class="dot d-k"></span></td><td><span class="dot d-b"></span></td><td><span class="dot d-g"></span></td><td><span class="dot d-b"></span></td></tr>
      <tr><td>Last Row</td><td><span class="dot d-b"></span></td><td><span class="dot d-b"></span></td><td><span class="dot d-g"></span></td><td><span class="dot d-b"></span></td></tr>
    </table>
    <h3 class="sub-title" style="top:299px;font-size:8.6px">Pie Chart Design Content</h3>
    <div class="copy" style="top:313px;right:186px"><p>Lorem Ipsum is simply dummy text of the printing and typesetting industry. Lorem Ipsum has been the industry's standard dummy text ever since the 1500s, when an unknown printer took a galley of type and scrambled it to.</p><p style="margin-top:13.5px">Lorem Ipsum is simply dummy text of the printing and typesetting industry. Lorem Ipsum has been the industry's standard dummy text ever</p></div>
    <svg style="position:absolute;left:180px;top:305px" width="170" height="170" viewBox="0 0 170 170" aria-label="Donut chart">
      <g transform="translate(81 82)" fill="none" stroke-width="34">
        <circle r="59" stroke="#5a5a5a" stroke-dasharray="82.4 370.7" transform="rotate(-150)"/>
        <circle r="59" stroke="#0b6fc4" stroke-dasharray="92.7 370.7" transform="rotate(-70)"/>
        <circle r="59" stroke="#c9c9c9" stroke-dasharray="51.5 370.7" transform="rotate(20)"/>
        <circle r="59" stroke="#0b6fc4" stroke-dasharray="92.7 370.7" transform="rotate(70)"/>
        <circle r="59" stroke="#3aa8f2" stroke-dasharray="51.5 370.7" transform="rotate(160)"/>
      </g>
      <g fill="#fff" font-family="Roboto, sans-serif" font-size="10" text-anchor="middle">
        <text x="77" y="46">20%</text>
        <text x="135" y="82">50%</text>
        <text x="131" y="142">20%</text>
        <text x="55" y="162">20%</text>
        <text x="25" y="83">40%</text>
      </g>
    </svg>
    <footer class="page-foot">Project summary: site address, lodgement reference and council area for this planning report.<br>Prepared for development assessment and review by local and state government authorities.</footer>
  </section>

  <section class="page" style="left:1133px;top:23px">
    <h2 class="page-title">Image Title here</h2>
    <div class="brand-tag"><div class="mark"></div><div class="name">URBAN PARCEL</div></div>
    <div class="photo" role="img" aria-label="Photograph of three people studying a map on a wooden table" style="left:13px;top:49px;width:325px;height:215px;background:linear-gradient(160deg,#b9a684 0%,#8a7658 45%,#d8d3c4 70%,#6d5a44 100%)"></div>
    <h3 class="sub-title" style="top:276px;font-weight:700;font-size:9.6px">Image Title here Image Title here Image Title here Image Title here</h3>
    <div class="copy" style="top:299px"><p>Lorem Ipsum is simply dummy text of the printing and typesetting industry. Lorem Ipsum has been the industry's standard dummy text ever since the 1500s, when an unknown printer took a galley of type and scrambled it to.</p><p style="margin-top:13.5px">Lorem Ipsum is simply dummy text of the printing and typesetting industry. Lorem Ipsum has been the industry's standard dummy text ever Lorem Ipsum is simply dummy text of the printing and typesetting industry. Lorem Ipsum has been the industry's standard dummy text ever since the 1500s, when an unknown printer took a galley of type and scrambled it to.</p><p style="margin-top:13.5px">Lorem Ipsum is simply dummy text of the printing and typesetting industry. Lorem Ipsum has been the industry's standard dummy text ever</p></div>
    <footer class="page-foot">Project summary: site address, lodgement reference and council area for this planning report.<br>Prepared for development assessment and review by local and state government authorities.</footer>
  </section>

  <section class="page" style="left:1508px;top:23px">
    <h2 class="page-title">Two Image Title here</h2>
    <div class="brand-tag"><div class="mark"></div><div class="name">URBAN PARCEL</div></div>
    <div class="pair-copy" style="top:65px"><h3 class="pair-title">Image Paragraph Title here Image Paragraph Title here</h3><p>Lorem Ipsum is simply dummy text of the printing and typesetting industry. Lorem Ipsum has been the industry's standard dummy text ever since the 1500s, when an unknown printer took a galley of type and scrambled it to Lorem Ipsum is simply dummy text of the printing</p></div>
    <div class="photo" role="img" aria-label="Photograph of a hand placing a piece on an architectural site model" style="left:195px;top:79px;width:148px;height:107px;background:linear-gradient(135deg,#5b4a3c 0%,#9a9a92 45%,#6f8a5a 75%,#c9c6bd 100%)"></div>
    <div class="pair-copy" style="top:205px"><h3 class="pair-title">Image Paragraph Title here Image Paragraph Title here</h3><p>Lorem Ipsum is simply dummy text of the printing and typesetting industry. Lorem Ipsum has been the industry's standard dummy text ever since the 1500s, when an unknown printer took a galley of type and scrambled it to Lorem Ipsum is simply dummy text of the printing</p></div>
    <div class="photo" role="img" aria-label="Photograph of a hand placing a piece on an architectural site model" style="left:195px;top:219px;width:148px;height:107px;background:linear-gradient(135deg,#5b4a3c 0%,#9a9a92 45%,#6f8a5a 75%,#c9c6bd 100%)"></div>
    <div class="pair-copy" style="top:350px"><h3 class="pair-title">Image Paragraph Title here Image Paragraph Title here</h3><p>Lorem Ipsum is simply dummy text of the printing and typesetting industry. Lorem Ipsum has been the industry's standard dummy text ever since the 1500s, when an unknown printer took a galley of type and scrambled it to Lorem Ipsum is simply dummy text of the printing</p></div>
    <div class="photo" role="img" aria-label="Photograph of a hand placing a piece on an architectural site model" style="left:195px;top:364px;width:148px;height:107px;background:linear-gradient(135deg,#5b4a3c 0%,#9a9a92 45%,#6f8a5a 75%,#c9c6bd 100%)"></div>
    <footer class="page-foot">Project summary: site address, lodgement reference and council area for this planning report.<br>Prepared for development assessment and review by local and state government authorities.</footer>
  </section>

  <section class="page section-page" style="left:22px;top:544px">
    <div class="rule" style="left:26px;top:206px;width:310px"></div>
    <div class="section-head" style="top:218px">
      <h2>Section Devide Here</h2>
      <div class="lede">sub section here</div>
    </div>
    <div class="rule" style="left:26px;top:284px;width:310px"></div>
    <footer class="page-foot">Project summary: site address, lodgement reference and council area for this planning report.<br>Prepared for development assessment and review by local and state government authorities.</footer>
  </section>

  <section class="page" style="left:391px;top:544px">
    <h2 class="page-title">Main Heading Here</h2>
    <div class="brand-tag"><div class="mark"></div><div class="name">URBAN PARCEL</div></div>
    <div class="copy" style="top:50px"><p>Lorem Ipsum is simply dummy text of the printing and typesetting industry. Lorem Ipsum has been the industry's standard dummy text ever since the 1500s, when an unknown printer took a galley of type and scrambled it to make a type specimen book. It has survived not only five centuries, but also the leap into electronic typesetting, remaining essentially unchanged. It was popularised in the 1960s with the release of Presstype sheets containing Lorem Ipsum passages, and more recently with desktop publishing software like Folio LayoutPro including versions of Lorem Ipsum.</p></div>
    <h3 class="sub-title" style="top:155px">Subheading Text Title here</h3>
    <div class="copy" style="top:173px"><p>Lorem Ipsum is simply dummy text of the printing and typesetting industry. Lorem Ipsum has been the industry's standard dummy text ever since the 1500s, when an unknown printer took a galley of type and scrambled it to make a type</p></div>
    <svg style="position:absolute;left:0;top:0" width="356" height="480" viewBox="0 0 356 480" aria-label="Bar chart">
      <g stroke="#cfcfcf" stroke-width="2">
        <line x1="64" y1="240" x2="302" y2="240"/><line x1="64" y1="276" x2="302" y2="276"/>
        <line x1="64" y1="312" x2="302" y2="312"/><line x1="64" y1="348" x2="302" y2="348"/>
        <line x1="64" y1="384" x2="302" y2="384"/><line x1="64" y1="420" x2="302" y2="420"/>
      </g>
      <g fill="#b5b5b5" font-family="Roboto, sans-serif" font-size="14" text-anchor="middle">
        <text x="38" y="262">60</text><text x="38" y="298">50</text><text x="38" y="334">40</text>
        <text x="38" y="370">30</text><text x="38" y="406">20</text><text x="38" y="442">10</text>
      </g>
      <g>
        <rect x="71" y="341" width="12" height="115" rx="6" fill="#5a5a5a"/>
        <rect x="89" y="268" width="12" height="188" rx="6" fill="#0b6fc4"/>
        <rect x="110" y="308" width="12" height="148" rx="6" fill="#3aa8f2"/>
        <rect x="141" y="341" width="12" height="115" rx="6" fill="#5a5a5a"/>
        <rect x="159" y="268" width="12" height="188" rx="6" fill="#0b6fc4"/>
        <rect x="180" y="308" width="12" height="148" rx="6" fill="#3aa8f2"/>
        <rect x="212" y="341" width="12" height="115" rx="6" fill="#5a5a5a"/>
        <rect x="230" y="268" width="12" height="188" rx="6" fill="#0b6fc4"/>
        <rect x="251" y="308" width="12" height="148" rx="6" fill="#3aa8f2"/>
        <rect x="271" y="341" width="12" height="115" rx="6" fill="#5a5a5a"/>
      </g>
      <polyline points="54,240 54,455 302,455" stroke="#c9c9c9" stroke-width="4" fill="none"/>
    </svg>
    <footer class="page-foot">Project summary: site address, lodgement reference and council area for this planning report.<br>Prepared for development assessment and review by local and state government authorities.</footer>
  </section>

  <section class="page" style="left:765px;top:544px">
    <h2 class="page-title">Graphs Data</h2>
    <div class="brand-tag"><div class="mark"></div><div class="name">URBAN PARCEL</div></div>
    <div class="copy" style="top:54px"><p>Lorem Ipsum is simply dummy text of the printing and typesetting industry. Lorem Ipsum has been the industry's standard dummy text ever since the 1500s, when an unknown printer took a galley of type and scrambled it to Lorem Ipsum is simply dummy text of the printing and typesetting industry. Lorem Ipsum has been the industry's standard dummy text ever since the 1500s Lorem Ipsum is simply dummy text of the printing and typesetting industry. Lorem Ipsum has been the industry's standard dummy text ever since the 1500s, when an unknown printer took a galley of type and scrambled it to Lorem Ipsum is simply dummy text of the printing and typesetting industry. Lorem Ipsum has been the industry's standard dummy text ever since the 1500s y. Lorem Ipsum has been the industry's standard dummy text ever sinc</p></div>
    <svg style="position:absolute;left:0;top:190px" width="200" height="180" viewBox="0 190 200 180" aria-label="Pyramid chart">
      <polygon points="96,198 117,240 75,240" fill="#3aa8f2"/>
      <polygon points="74,243 118,243 144,294 48,294" fill="#0b6fc4"/>
      <polygon points="47,297 145,297 162,328 30,328" fill="#5a5a5a"/>
      <polygon points="29,331 163,331 179,362 13,362" fill="#c9c9c9"/>
      <g fill="#fff" font-family="Roboto, sans-serif" font-size="10" text-anchor="middle">
        <text x="96" y="232">10%</text><text x="96" y="283">50%</text>
        <text x="96" y="320">30%</text><text x="96" y="357">10%</text>
      </g>
    </svg>
    <div class="legend" style="top:218px"><div class="swatch" style="background:var(--graphite)"></div><div>Legend note describing the planning category shown here.</div></div>
    <div class="legend" style="top:258px"><div class="swatch" style="background:var(--blue)"></div><div>Legend note describing the planning category shown here.</div></div>
    <div class="legend" style="top:301px"><div class="swatch" style="background:var(--sky)"></div><div>Legend note describing the planning category shown here.</div></div>
    <div class="legend" style="top:341px"><div class="swatch" style="background:var(--mist)"></div><div>Legend note describing the planning category shown here.</div></div>
    <div class="copy" style="top:383px"><p>Lorem Ipsum is simply dummy text of the printing and typesetting industry. Lorem Ipsum has been the industry's standard dummy text ever since the 1500s, when an unknown printer took a galley of type and scrambled it to Lorem Ipsum is simply dummy text of the printing and typesetting industry. Lorem Ipsum has been the industry's standard dummy text ever since the 1500s Lorem Ipsum is simply dummy text of the printing and typesetting industry. Lorem Ipsum has been the industry's standard</p></div>
    <footer class="page-foot">Project summary: site address, lodgement reference and council area for this planning report.<br>Prepared for development assessment and review by local and state government authorities.</footer>
  </section>

  <section class="page" style="left:1133px;top:544px">
    <h2 class="page-title">Graphs Data</h2>
    <div class="brand-tag"><div class="mark"></div><div class="name">URBAN PARCEL</div></div>
    <div class="copy" style="top:54px"><p>Lorem Ipsum is simply dummy text of the printing and typesetting industry. Lorem Ipsum has been the industry's standard dummy text ever since the 1500s, when an unknown printer took a galley of type and scrambled it to Lorem Ipsum is simply dummy text of the printing and typesetting industry. Lorem Ipsum has been the industry's standard dummy text ever since the 1500s</p></div>
    <svg style="position:absolute;left:0;top:0" width="356" height="390" viewBox="0 0 356 390" aria-label="Peak chart">
      <g stroke="#cfcfcf" stroke-width="2">
        <line x1="67" y1="144" x2="318" y2="144"/><line x1="67" y1="182" x2="318" y2="182"/>
        <line x1="67" y1="220" x2="318" y2="220"/><line x1="67" y1="258" x2="318" y2="258"/>
        <line x1="67" y1="296" x2="318" y2="296"/><line x1="67" y1="334" x2="318" y2="334"/>
      </g>
      <g fill="#b5b5b5" font-family="Roboto, sans-serif" font-size="14" text-anchor="middle">
        <text x="39" y="167">60</text><text x="39" y="206">50</text><text x="39" y="244">40</text>
        <text x="39" y="282">30</text><text x="39" y="320">20</text><text x="39" y="358">10</text>
      </g>
      <path d="M79 354 L104 232 Q107 222 110 232 L137 354 Z" fill="#5a5a5a"/>
      <path d="M111 354 L156 152 Q160 138 164 152 L212 354 Z" fill="#0b6fc4"/>
      <path d="M179 354 L199 264 Q202 254 205 264 L225 354 Z" fill="#3aa8f2"/>
      <path d="M219 354 L241 238 Q244 228 247 238 L272 354 Z" fill="#0b6fc4"/>
      <path d="M257 354 L268 266 Q270 256 272 266 L285 354 Z" fill="#5a5a5a"/>
      <path d="M272 354 L287 305 Q289 298 291 305 L305 354 Z" fill="#3aa8f2"/>
      <polyline points="58,144 58,371 318,371" stroke="#c9c9c9" stroke-width="4" fill="none"/>
    </svg>
    <div class="copy" style="top:397px"><p>Lorem Ipsum is simply dummy text of the printing and typesetting industry. Lorem Ipsum has been the industry's standard dummy text ever since the 1500s, when an unknown printer took a galley of type and scrambled it to Lorem Ipsum is simply dummy text of the printing and typesetting industry. Lorem Ipsum has been the industry's standard dummy text ever since the 1500s</p></div>
    <footer class="page-foot">Project summary: site address, lodgement reference and council area for this planning report.<br>Prepared for development assessment and review by local and state government authorities.</footer>
  </section>

  <div class="foot-tab" style="left:1420px;top:533px"></div>
  <div class="foot-tab" style="left:1798px;top:533px"></div>
  <div class="foot-tab" style="left:1052px;top:1053px"></div>
  <div class="foot-tab" style="left:1423px;top:1053px"></div>

  <section class="thanks">
    <div class="lockup" style="left:76px;top:170px;gap:14px">
      <div class="mark" style="background:#fff;width:46px;height:46px"></div>
      <div class="name" style="color:#fff;font-size:24px;line-height:28px">URBAN<br>PARCEL</div>
    </div>
    <div class="rule" style="left:7px;top:247px;width:340px"></div>
    <div class="title">
      <h2>Thanks for your Time</h2>
      <div class="lede">Report sub details here</div>
    </div>
    <div class="rule" style="left:7px;top:318px;width:340px"></div>
    <div class="address">Address Details Here<br>Address Details Here<br>Address Details Here</div>
    <div class="fine">Project summary: site address, lodgement reference and council area for this planning report.<br>Prepared for development assessment and review by local and state government authorities.</div>
  </section>

  <article class="letter" style="left:40px;top:1108px;width:537px;height:752px">
    <div style="position:absolute;left:0;right:0;top:17px;height:12px;background:var(--cyan)"></div>
    <div style="position:absolute;left:0;right:0;top:32px;height:2px;background:#cfcfcf"></div>
    <div class="lockup" style="left:322px;top:56px">
      <div class="mark" style="background:var(--cyan)"></div>
      <div class="name" style="color:var(--navy)">URBAN<br>PARCEL</div>
    </div>
    <div class="recipient" style="left:74px;top:154px">
      <div class="to">To,</div>
      <div class="who">DANIEL FOSTER</div>
      <div class="role">Managing Director</div>
      <div class="line"><span class="key">P:</span> +1-555-204-7391</div>
      <div class="line"><span class="key">W:</span> www.examplestudio.com</div>
      <div class="line"><span class="key">A:</span> 218 Maple Court<br>Riverton, NJ 08077</div>
    </div>
    <div class="letter-date" style="right:74px;top:226px"><span class="key">DATE:</span>21 April, 2030</div>
    <div class="salutation" style="left:74px;top:265px">DEAR SIR,</div>
    <div class="letter-copy" style="left:74px;top:289px;width:389px">
      <p>Lorem Ipsum is simply dummy text of the printing and typesetting industry. Lorem Ipsum has been the industry's standard dummy text ever since the 1500s, when an unknown printer took a galley of type and scrambled it to make a type specimen book. It has survived not only five centuries, but also the leap into electronic typesetting, remaining essentially unchanged.</p>
      <p>It was popularised in the 1960s with the release of Presstype sheets containing Lorem Ipsum passages, and more recently with desktop publishing software like Folio LayoutPro including versions of Lorem Ipsum.</p>
      <p>It is a long established fact that a reader will be distracted by the readable content of a page when looking at its layout. The point of using Lorem Ipsum is that it has a more-or-less normal distribution of letters, as opposed to using 'Content here, content here', making it look like readable English. Many desktop publishing packages and web page editors now use Lorem Ipsum as their default model text, and a search for 'lorem ipsum' will uncover many web sites still in their infancy. Various versions have evolved over the years, sometimes by accident, sometimes on purpose (injected humour and the like).</p>
    </div>
    <div class="sender" style="left:74px;top:544px">
      <div class="from">From,</div>
      <div class="who">OLIVER GRANT</div>
      <div class="role">Creative Designer</div>
    </div>
    <div class="signature" role="img" aria-label="Handwritten signature" style="left:78px;top:587px"></div>
    <div class="sign-line" style="left:74px;top:611px"></div>
    <div class="sign-label" style="left:80px;top:618px">SIGNATURE</div>
    <div class="letter-foot" style="top:695px;height:57px;background:var(--letter-dark)">
      <div class="contact" style="left:109px;top:-10px;width:100px">
        <span class="icon-ring" style="margin:0 auto 4px"><svg viewBox="0 0 24 24"><path d="M6.6 10.8a15 15 0 0 0 6.6 6.6l2.2-2.2a1 1 0 0 1 1-.25 11.4 11.4 0 0 0 3.6.57 1 1 0 0 1 1 1V20a1 1 0 0 1-1 1A17 17 0 0 1 3 4a1 1 0 0 1 1-1h3.5a1 1 0 0 1 1 1 11.4 11.4 0 0 0 .57 3.6 1 1 0 0 1-.25 1z" fill="#13b4ee"/></svg></span>
        +1-555-310-4426<br>+1-555-381-2290
      </div>
      <div class="contact" style="left:199px;top:-10px;width:120px">
        <span class="icon-ring" style="margin:0 auto 4px"><svg viewBox="0 0 24 24" fill="none" stroke="#13b4ee" stroke-width="2"><circle cx="12" cy="12" r="9"/><path d="M3 12h18M12 3c3 3 3 15 0 18M12 3c-3 3-3 15 0 18"/></svg></span>
        www.examplestudio.com<br>hello@examplestudio.com
      </div>
      <div class="contact" style="left:318px;top:-10px;width:110px">
        <span class="icon-ring" style="margin:0 auto 4px"><svg viewBox="0 0 24 24"><path d="M12 2a7 7 0 0 0-7 7c0 5 7 13 7 13s7-8 7-13a7 7 0 0 0-7-7zm0 9.5A2.5 2.5 0 1 1 12 6.5a2.5 2.5 0 0 1 0 5z" fill="#13b4ee"/></svg></span>
        52 Harbor Lane<br>Easton, MI 48110
      </div>
    </div>
  </article>

  <article class="letter" style="left:615px;top:1101px;width:548px;height:768px">
    <div style="position:absolute;left:0;right:0;top:0;height:69px;background:var(--cyan)"></div>
    <div style="position:absolute;left:0;right:0;top:72px;height:2px;background:#c4c4c4"></div>
    <div style="position:absolute;left:347px;top:32px;width:180px;height:57px;background:#fff">
      <div class="lockup" style="left:14px;top:10px">
        <div class="mark" style="background:var(--cyan)"></div>
        <div class="name" style="color:var(--navy)">URBAN<br>PARCEL</div>
      </div>
    </div>
    <div class="recipient" style="left:75px;top:158px">
      <div class="to">To,</div>
      <div class="who">DANIEL FOSTER</div>
      <div class="role">Managing Director</div>
      <div class="line"><span class="key">P:</span> +1-555-204-7391</div>
      <div class="line"><span class="key">W:</span> www.examplestudio.com</div>
      <div class="line"><span class="key">A:</span> 218 Maple Court<br>Riverton, NJ 08077</div>
    </div>
    <div class="letter-date" style="right:75px;top:232px"><span class="key">DATE:</span>21 April, 2030</div>
    <div class="salutation" style="left:75px;top:271px">DEAR SIR,</div>
    <div class="letter-copy" style="left:75px;top:296px;width:398px">
      <p>Lorem Ipsum is simply dummy text of the printing and typesetting industry. Lorem Ipsum has been the industry's standard dummy text ever since the 1500s, when an unknown printer took a galley of type and scrambled it to make a type specimen book. It has survived not only five centuries, but also the leap into electronic typesetting, remaining essentially unchanged.</p>
      <p>It was popularised in the 1960s with the release of Presstype sheets containing Lorem Ipsum passages, and more recently with desktop publishing software like Folio LayoutPro including versions of Lorem Ipsum.</p>
      <p>It is a long established fact that a reader will be distracted by the readable content of a page when looking at its layout. The point of using Lorem Ipsum is that it has a more-or-less normal distribution of letters, as opposed to using 'Content here, content here', making it look like readable English. Many desktop publishing packages and web page editors now use Lorem Ipsum as their default model text, and a search for 'lorem ipsum' will uncover many web sites still in their infancy. Various versions have evolved over the years, sometimes by accident, sometimes on purpose (injected humour and the like).</p>
    </div>
    <div class="sender" style="left:75px;top:555px">
      <div class="from">From,</div>
      <div class="who">OLIVER GRANT</div>
      <div class="role">Creative Designer</div>
    </div>
    <div class="signature" role="img" aria-label="Handwritten signature" style="left:79px;top:598px"></div>
    <div class="sign-line" style="left:75px;top:623px"></div>
    <div class="sign-label" style="left:81px;top:631px">SIGNATURE</div>
    <div class="letter-foot" style="top:691px;height:77px;background:var(--cyan)">
      <div class="contact-row" style="left:75px;top:24px">
        <span class="icon-ring"><svg viewBox="0 0 24 24"><path d="M6.6 10.8a15 15 0 0 0 6.6 6.6l2.2-2.2a1 1 0 0 1 1-.25 11.4 11.4 0 0 0 3.6.57 1 1 0 0 1 1 1V20a1 1 0 0 1-1 1A17 17 0 0 1 3 4a1 1 0 0 1 1-1h3.5a1 1 0 0 1 1 1 11.4 11.4 0 0 0 .57 3.6 1 1 0 0 1-.25 1z" fill="#13b4ee"/></svg></span>
        <span>+1-555-310-4426<br>+1-555-381-2290</span>
      </div>
      <div class="contact-row" style="left:196px;top:24px">
        <span class="icon-ring"><svg viewBox="0 0 24 24" fill="none" stroke="#13b4ee" stroke-width="2"><circle cx="12" cy="12" r="9"/><path d="M3 12h18M12 3c3 3 3 15 0 18M12 3c-3 3-3 15 0 18"/></svg></span>
        <span style="text-align:center">www.examplestudio.com<br>hello@examplestudio.com</span>
      </div>
      <div class="contact-row" style="left:347px;top:24px">
        <span class="icon-ring"><svg viewBox="0 0 24 24"><path d="M12 2a7 7 0 0 0-7 7c0 5 7 13 7 13s7-8 7-13a7 7 0 0 0-7-7zm0 9.5A2.5 2.5 0 1 1 12 6.5a2.5 2.5 0 0 1 0 5z" fill="#13b4ee"/></svg></span>
        <span style="text-align:center">52 Harbor Lane<br>Easton, MI 48110</span>
      </div>
    </div>
  </article>

</div>
</body>
</html>
```